Business Card for a Floral & Decorating Business

I would like to take my current logo and create a better business card. I am looking for elegance as I am a florist and event decorator. My logo has multiple colour options. I like colours like green, purple, pink and orange, I think I would like a white card, open to black back ground. I want it to feel elegant and romantic. I like metallic lettering that maybe is indented in the paper, I also like glossy paper. I have a full logo already as well as a badge. I have attached both in multiple colours.m
Updates

Need extra days to review

Target Market(s)

Weddings, special events, floral customers

Industry/Entity Type

Floral and decorating

Contact Information for Business Card

Phone number, email, instagram, facebook, title, name, logo

Font styles to use
Script

Requirements
Nice to have
• Elegant

```html
<!DOCTYPE html>
<html lang="en">
<head>
<meta charset="utf-8">
<title>Marlow Ashby – Business Card</title>
<link href="https://fonts.googleapis.com/css2?family=Great+Vibes&family=Cormorant+Garamond:wght@500&family=Noto+Sans:wght@400&display=swap" rel="stylesheet">
<style>
  :root{
    --backdrop:#ababab;
    --rose:#bb8c7c;
    --rose-deep:#b07f70;
    --blush:#e6c3b8;
    --blush-strong:#e2b5a3;
    --paper:#ffffff;
    --ink:#3d3d3d;
  }
  *{margin:0;padding:0;box-sizing:border-box}
  html,body{width:1200px;height:1000px;overflow:hidden;background:var(--backdrop)}
  .canvas{position:relative;width:1200px;height:1000px}
  .card{position:absolute;top:184px;width:355px;height:614px;overflow:hidden}
  .card--front{left:149px;background:var(--rose)}
  .card--back{left:627px;background:var(--paper)}

  .floral-band{position:absolute;left:0;width:100%}
  .floral-band--top{top:0;height:150px;background:linear-gradient(180deg,var(--rose-deep),var(--rose))}
  .floral-band--bottom{bottom:0;height:160px;background:linear-gradient(0deg,var(--rose-deep),var(--rose))}

  .front-mark{position:absolute;left:0;top:225px;width:100%;text-align:center}
  .front-mark__dot{display:block;margin:0 auto 6px;width:50px;height:50px;border:1px solid var(--blush);border-radius:50%}
  .front-mark__name{font-family:"Great Vibes",cursive;font-size:46px;color:var(--blush);line-height:1}
  .front-mark__tag{margin-top:6px;font-family:"Cormorant Garamond",serif;font-size:10px;letter-spacing:3px;color:var(--blush)}

  .badge{position:absolute;left:77px;top:65px;width:201px;height:201px;border:1px solid var(--blush-strong);border-radius:50%;display:flex;flex-direction:column;align-items:center;justify-content:center;text-align:center}
  .badge__name{font-family:"Cormorant Garamond",serif;font-size:20px;letter-spacing:2px;color:var(--blush-strong)}
  .badge__place{margin-top:6px;font-family:"Cormorant Garamond",serif;font-size:10px;letter-spacing:3px;color:var(--blush-strong)}

  .back-name{position:absolute;left:0;top:285px;width:100%;font-family:"Great Vibes",cursive;color:var(--blush-strong);font-size:64px;line-height:1}
  .back-name__first{position:absolute;left:60px;top:0}
  .back-name__last{position:absolute;left:140px;top:44px}

  .contact{position:absolute;left:0;width:100%;text-align:center;font-family:"Noto Sans",sans-serif;font-size:14px;color:var(--ink);line-height:18px}
  .contact--direct{top:434px}
  .contact--social{top:507px}
  .contact__icons{display:flex;justify-content:center;gap:7px;margin-bottom:7px}
  .contact__icons svg{width:20px;height:20px}
</style>
</head>
<body>
<main class="canvas">
  <section class="card card--front">
    <div class="floral-band floral-band--top" role="img" aria-label="Faint line-drawn flowers and leaves along the top edge"></div>
    <div class="front-mark">
      <span class="front-mark__dot"></span>
      <div class="front-mark__name">marlow ashby</div>
      <div class="front-mark__tag">DECORATING &amp; FLORALS</div>
    </div>
    <div class="floral-band floral-band--bottom" role="img" aria-label="Faint line-drawn flowers and leaves along the bottom edge"></div>
  </section>

  <section class="card card--back">
    <div class="badge">
      <div class="badge__name">MARLOW ASHBY</div>
      <div class="badge__place">CEDAR VALE, ON</div>
    </div>
    <h1 class="back-name"><span class="back-name__first">marlow</span><span class="back-name__last">ashby</span></h1>

    <div class="contact contact--direct">
      <div class="contact__icons">
        <svg viewBox="0 0 20 20" aria-label="Phone"><rect x="1" y="1" width="18" height="18" rx="4" fill="none" stroke="#3d3d3d" stroke-width="1.6"/><path d="M6.5 5.5l2 .3.7 2.2-1.2 1a7 7 0 0 0 3 3l1-1.2 2.2.7.3 2-1.3 1.2A9 9 0 0 1 5.3 6.8z" fill="none" stroke="#3d3d3d" stroke-width="1.3" stroke-linejoin="round"/></svg>
        <svg viewBox="0 0 20 20" aria-label="Email"><rect x="1" y="1" width="18" height="18" rx="4" fill="none" stroke="#3d3d3d" stroke-width="1.6"/><rect x="4.5" y="6" width="11" height="8" fill="none" stroke="#3d3d3d" stroke-width="1.3"/><path d="M4.5 6l5.5 4.5L15.5 6M4.5 14l4-3.5M15.5 14l-4-3.5" fill="none" stroke="#3d3d3d" stroke-width="1.3"/></svg>
      </div>
      <div>(555) 013-4821</div>
      <div>marlowashby@example.com</div>
    </div>

    <div class="contact contact--social">
      <div class="contact__icons">
        <svg viewBox="0 0 20 20" aria-label="Social profile"><circle cx="10" cy="10" r="8.5" fill="none" stroke="#3d3d3d" stroke-width="1.6"/></svg>
        <svg viewBox="0 0 20 20" aria-label="Social page"><circle cx="10" cy="10" r="8.5" fill="none" stroke="#3d3d3d" stroke-width="1.6"/></svg>
      </div>
      <div>marlowashbydecorating.florals</div>
      <div>simplyyoursdecorating</div>
    </div>
  </section>
</main>
</body>
</html>
```